Harbor Emberlights - Woodwick candles needing a sylish box designed

We need a box designed for our woodwick candles.
I would like to see a box that looks very stylish and I would like the logo to be in a silver foil outlined box (I will include photos of examples). I like a box that has a silver foil edge around it, though not essential. A pattern of some sort would be nice on the box, staying with the wood/beach theme. I will also need to include other information on the back of the box about the candle (can I do this after I see the design?). I need to be able to change the fragrance when needed on the box label. The box size is L105mm W105mm H128mm. I am really open to any ideas. Looking for something very stylish and luxurious looking.
The lids on my candles are silver and the candles have a wooden wick.

Target Market(s)

Department stores and retail shops

Industry/Entity Type

Retail

Colors
ffffff

Requirements
Must have
• Looking for something very stylish and luxurious looking, that will look and fit great in any large department store.
Nice to have
• Wooden look, if possible.
• Clean and crisp look. Very pretty.

```html
<!DOCTYPE html>
<html lang="en">
<head>
<meta charset="utf-8">
<title>Harbor Emberlights – Candle Box Dieline</title>
<link rel="stylesheet" href="https://fonts.googleapis.com/css2?family=Cinzel:wght@400;500&family=Exo+2:ital,wght@1,300&display=swap">
<style>
  :root {
    --paper: #ffffff;
    --cut-line: #1a1a1a;
    --ink: #1c1c1c;
    --label-black: #050505;
    --foil-silver: #c9c9c9;
    --foil-light: #eeeeee;
    --sea-deep: #0c3a8c;
    --sea-mid: #1e8dd0;
    --sea-turquoise: #3db6d6;
    --surf: #c4dcd9;
    --sand: #d4b287;
  }
  html, body {
    margin: 0;
    padding: 0;
    width: 1200px;
    height: 1066px;
    overflow: hidden;
    background: var(--paper);
  }
  .dieline {
    display: block;
    width: 1200px;
    height: 1066px;
  }
  .cut { fill: none; stroke: var(--cut-line); stroke-width: 1.1; }
  .panel { fill: var(--paper); }
  .brand-name {
    font-family: "Cinzel", serif;
    font-variant: small-caps;
    letter-spacing: 1.2px;
  }
  .brand-name--panel { fill: var(--ink); font-size: 12px; }
  .brand-name--label { fill: var(--foil-silver); font-size: 11px; }
  .fragrance-name {
    font-family: "Cinzel", serif;
    fill: var(--foil-light);
    font-size: 14px;
    letter-spacing: 0.8px;
  }
  .about-copy {
    font-family: "Exo 2", sans-serif;
    font-style: italic;
    font-weight: 300;
    font-size: 10.4px;
    fill: var(--ink);
  }
  .label-card { fill: var(--label-black); }
  .label-foil { fill: none; stroke: var(--foil-silver); stroke-width: 3; }
</style>
</head>
<body>
<svg class="dieline" viewBox="0 0 1273 1131" preserveAspectRatio="xMidYMid meet" xmlns="http://www.w3.org/2000/svg">
  <defs>
    <linearGradient id="shoreline" x1="0" y1="0" x2="0" y2="1">
      <stop offset="0" stop-color="var(--sea-deep)"/>
      <stop offset="0.16" stop-color="var(--sea-mid)"/>
      <stop offset="0.45" stop-color="var(--sea-turquoise)"/>
      <stop offset="0.74" stop-color="var(--surf)"/>
      <stop offset="1" stop-color="var(--sand)"/>
    </linearGradient>
  </defs>

  <!-- shoreline band across the four walls -->
  <rect class="shore-band" x="21" y="594" width="1190" height="157" fill="url(#shoreline)"
        role="img" aria-label="Photograph of turquoise ocean waves rolling onto a sandy beach"/>

  <!-- glue and dust flaps -->
  <g class="flaps">
    <polygon class="cut" points="21,90 43,49 298,49 318,90"/>
    <polygon class="cut" points="318,388 337,353 598,353 616,388"/>
    <polygon class="cut" points="914,388 933,353 1193,353 1211,388"/>
    <polygon class="cut" points="318,751 338,786 597,786 616,751"/>
    <polygon class="cut" points="914,751 933,786 1193,786 1211,751"/>
    <polygon class="cut" points="1211,388 1253,410 1253,729 1211,751"/>
    <polygon class="cut" points="616,1049 636,1090 894,1090 914,1049"/>
  </g>

  <!-- box faces -->
  <g class="faces">
    <rect class="cut" x="21" y="90" width="297" height="298"/>
    <rect class="cut" x="21" y="388" width="297" height="363"/>
    <rect class="cut" x="318" y="388" width="298" height="363"/>
    <rect class="cut" x="616" y="388" width="298" height="363"/>
    <rect class="cut" x="914" y="388" width="297" height="363"/>
    <rect class="cut" x="616" y="751" width="298" height="298"/>
  </g>

  <!-- back wall: about copy and brand -->
  <g class="back-wall">
    <text class="about-copy" text-anchor="middle">
      <tspan x="170" y="435">A candle is an ignitable wick embedded in wax</tspan>
      <tspan x="170" y="448">or another flammable solid substance such as</tspan>
      <tspan x="170" y="461">tallow that provides light, and in some cases, a</tspan>
      <tspan x="170" y="474">fragrance. It can also be used to provide heat,</tspan>
      <tspan x="170" y="488">or used as a method of keeping time.</tspan>
    </text>
    <text class="brand-name brand-name--panel" x="170" y="571" text-anchor="middle">Harbor Emberlights</text>
  </g>

  <!-- front wall: foil-framed fragrance label -->
  <g class="front-label">
    <rect class="label-card" x="686" y="417" width="158" height="156"/>
    <rect class="label-foil" x="694.5" y="425.5" width="141" height="140"/>
    <text class="brand-name brand-name--label" x="765" y="496" text-anchor="middle">Harbor Emberlights</text>
    <text class="fragrance-name" x="765" y="543" text-anchor="middle">PINE LIME</text>
  </g>
</svg>
</body>
</html>
```